REVISED : Logo & Stationery design for Naturopath

1. I need a logo and stationery (A4 letterhead, Business card & postcard size card for voucher/birthday/reminder use) for my new clinic. 
2. Overall look / logo needs to achieve: sense of personal attention (handwriting like script use somewhere), be unfussy, elegant, professional, modern. calm.
3. MUST be DIFFERENT to what we normally see for naturopaths.
4. Logo will be used eventually on new website so must lend itself to that use.
5. Possible tag lines 'Health is in your nature' or 'Health for generations' = general themes
6. Should appeal to men, mothers, women, depressed, families
Please feel free to submit logo designs prior to stationery work up if preferred.  

Thanks for your designs.  I have updated my brief a little, I hope that it now gives a clearer picture of what I'm looking for.  Have a great day! Marion

Hi Everyone.  I have uploaded some dandelion to give you an idea of the symmetry, perfection and airiness that I'm looking for.

heading away for a week, so apologies to extend the deadline.  Decision will be made on Friday.  Thanks for your patience.

My clients are aged from 5m to 75 years and have an array of problems. My main interest is joint and general inflammation and the role of genetic heritage and nutrigenomics. I follow an evidence based approach. Have a look at www.marionkestle.com.au

Must have
1. some script based font 
2.  colours of nature . 
3. Trading Name: Marion Kestle Naturopathy 
4. Company Name: Brightwell Stride Partners Pty Ltd ABN: 58 217 630 914 (these must be on for legal reasons but not form part of logo or overall company name. 
5. Mailing Address: PO Box 4392, Tallow Ridge NSW 1590 
6. Clinic Address: TBC 
7. Tel: 1300 48 29 63 
8. e: naturopathy@marionkestle.com.au 
9. w: marionkestle.com.au
Business Card and Postcard do not need ABN & Pty Ltd name.
Business Card should have my qualifications: Bachelor of Health Science (Complementary Medicine), ND.
Nice to have
1. design able to be embossed (card, business card)
2. able to be used on non-bleached recycled paper 
3. suitable of matt / uncoated card
4. good for vegetable dye printing
5. concept I really like is of a dandelion blowing in the wind (themes = herb, wistful, dissemination of information, free and easy) 
6. also really like idea of a 'tree of life'
7. but your interpretation of something entirely different might be a winner
8. Use of either of the tag lines 
9. Monochromatic 
Should not have
1. photos
2. more than 3 colours
3. Leaves (too much like every other Naturopath)

```html
<!DOCTYPE html>
<html lang="en">
<head>
<meta charset="utf-8">
<title>Marion Kestle Naturopathy – Stationery</title>
<link rel="stylesheet" href="https://fonts.googleapis.com/css2?family=Tinos:wght@400&display=swap">
<style>
  :root {
    --blush: #ebd0c6;
    --blush-light: #f3e2dc;
    --rose: #a86a68;
    --rose-soft: #cf9f96;
    --maroon: #5a1d1a;
    --ink: #3f1714;
    --espresso: #341210;
    --paper: #ffffff;
    --card-line: #e3cbc3;
  }
  * { margin: 0; padding: 0; box-sizing: border-box; }
  html, body { width: 848px; height: 1200px; overflow: hidden; background: var(--paper); }
  body { position: relative; font-family: "Tinos", "Times New Roman", serif; color: var(--ink); }

  .wordmark { white-space: nowrap; color: var(--maroon); }
  .wordmark span { display: block; }

  .illustration {
    position: absolute;
    background: radial-gradient(ellipse at 50% 45%, rgba(255,255,255,0.75) 0%, rgba(255,255,255,0.35) 45%, rgba(255,255,255,0) 72%);
    border-radius: 50%;
  }
  .illustration--on-white {
    background: radial-gradient(ellipse at 50% 45%, rgba(235,208,198,0.8) 0%, rgba(235,208,198,0.35) 50%, rgba(235,208,198,0) 72%);
  }

  /* Letterhead band */
  .letterhead { position: absolute; left: 0; top: 0; width: 848px; height: 205px; }
  .letterhead__field { position: absolute; left: 0; top: 0; width: 100%; height: 174px; background: var(--blush); }
  .letterhead__drift { position: absolute; left: 380px; top: 10px; width: 468px; height: 160px; }
  .letterhead__stripe { position: absolute; left: 0; top: 174px; width: 100%; height: 14px; background: var(--rose); }
  .letterhead__base { position: absolute; left: 0; top: 188px; width: 100%; height: 17px; background: var(--espresso); }
  .letterhead__art { left: 55px; top: 4px; width: 250px; height: 185px; }
  .letterhead__name { position: absolute; left: 176px; top: 86px; font-size: 33px; line-height: 37px; }
  .letterhead__name span + span { padding-left: 12px; }
  .letterhead__company { position: absolute; left: 535px; top: 70px; font-size: 25px; line-height: 28px; white-space: nowrap; color: var(--ink); }
  .letterhead__contact { position: absolute; left: 535px; top: 101px; font-size: 12.4px; line-height: 16px; white-space: nowrap; letter-spacing: -0.1px; color: var(--ink); }

  /* Postcard */
  .postcard {
    position: absolute; left: 296px; top: 243px; width: 426px; height: 604px;
    background: var(--blush); transform-origin: 0 0; transform: rotate(27.6deg);
  }
  .postcard__art-top { left: 40px; top: 40px; width: 360px; height: 170px; }
  .postcard__art-main { left: 50px; top: 300px; width: 280px; height: 300px; }
  .postcard__name { position: absolute; left: 125px; top: 170px; font-size: 40px; line-height: 46px; }
  .postcard__name span + span { padding-left: 22px; }
  .postcard__contact { position: absolute; left: 22px; top: 505px; font-size: 12.5px; line-height: 15px; white-space: nowrap; color: var(--ink); }

  /* Business card */
  .business-card {
    position: absolute; left: 398px; top: 683px; width: 350px; height: 200px;
    background: var(--paper); border: 1px solid var(--card-line);
  }
  .business-card__art { left: 4px; top: 6px; width: 190px; height: 145px; }
  .business-card__person { position: absolute; right: 10px; top: 12px; text-align: right; color: var(--rose-soft); }
  .business-card__holder { font-size: 19px; line-height: 20px; }
  .business-card__credentials { font-size: 6px; line-height: 7.5px; margin-top: 3px; }
  .business-card__name { position: absolute; left: 90px; top: 58px; font-size: 25px; line-height: 30px; }
  .business-card__name span + span { padding-left: 4px; }
  .business-card__company { position: absolute; left: 93px; top: 135px; font-size: 12px; white-space: nowrap; color: var(--rose-soft); }
  .business-card__contact { position: absolute; left: 93px; top: 151px; font-size: 7.2px; line-height: 9.6px; white-space: nowrap; color: var(--rose-soft); }

  /* Footer wave */
  .footer-drift { position: absolute; left: 0; top: 1020px; width: 848px; height: 180px; }
</style>
</head>
<body>

<header class="letterhead">
  <div class="letterhead__field"></div>
  <svg class="letterhead__drift" viewBox="0 0 468 160" role="img" aria-label="Soft flowing line pattern with drifting seeds across the band">
    <defs>
      <linearGradient id="drift-top" x1="0" y1="0" x2="1" y2="0">
        <stop offset="0" stop-color="#f3e2dc" stop-opacity="0"/>
        <stop offset="1" stop-color="#f3e2dc" stop-opacity="0.8"/>
      </linearGradient>
    </defs>
    <path d="M0 130 C120 70 220 160 330 90 C390 50 430 40 468 30 L468 70 C420 80 380 100 330 130 C230 180 120 120 0 150 Z" fill="url(#drift-top)"/>
  </svg>
  <div class="illustration letterhead__art" role="img" aria-label="Line drawing of dandelion seeds blowing in the wind"></div>
  <div class="letterhead__stripe"></div>
  <div class="letterhead__base"></div>

  <div class="wordmark letterhead__name"><span>Marion Kestle</span><span>Naturopathy</span></div>
  <div class="letterhead__company">Brightwell Stride Partners</div>
  <div class="letterhead__contact">
    Mailing Address: PO Box 4392, Tallow Ridge NSW 1590<br>
    Clinic Address: TBC Tel: 1800 48 29 63<br>
    email: naturopathy@marionkestle.com.au<br>
    website: marionkestle.com.au
  </div>
</header>

<section class="postcard">
  <div class="illustration postcard__art-top" role="img" aria-label="Cluster of dandelion seeds drifting across the card"></div>
  <div class="illustration postcard__art-main" role="img" aria-label="Large single dandelion seed line drawing"></div>
  <div class="wordmark postcard__name"><span>Marion Kestle</span><span>Naturopathy</span></div>
  <div class="postcard__contact">
    Mailing Address: PO Box 4392, Tallow Ridge NSW 1590<br>
    Clinic Address: TBC Tel: 1800 48 29 63<br>
    email: naturopathy@marionkestle.com.au<br>
    website: marionkestle.com.au
  </div>
</section>

<section class="business-card">
  <div class="illustration illustration--on-white business-card__art" role="img" aria-label="Line drawing of three dandelion seeds"></div>
  <div class="business-card__person">
    <div class="business-card__holder">Marion Kestle</div>
    <div class="business-card__credentials">Bachelor of Health Science<br>(Complementary Medicine), ND</div>
  </div>
  <div class="wordmark business-card__name"><span>Marion Kestle</span><span>Naturopathy</span></div>
  <div class="business-card__company">Brightwell Stride Partners</div>
  <div class="business-card__contact">
    PO Box 4392, Tallow Ridge NSW 1590<br>
    Tel: 1300 48 29 63<br>
    Email: naturopathy@marionkestle.com.au<br>
    Website: marionkestle.com.au
  </div>
</section>

<svg class="footer-drift" viewBox="0 0 848 180" role="img" aria-label="Fine flowing line pattern sweeping across the foot of the page">
  <defs>
    <linearGradient id="drift-foot" x1="0" y1="0" x2="0" y2="1">
      <stop offset="0" stop-color="#f0dcd6" stop-opacity="0.9"/>
      <stop offset="1" stop-color="#f6e8e3" stop-opacity="0.6"/>
    </linearGradient>
  </defs>
  <path d="M0 0 C150 10 260 90 430 95 C600 100 720 60 848 70 L848 180 C700 150 560 175 420 140 C260 100 130 60 0 60 Z" fill="url(#drift-foot)"/>
</svg>

</body>
</html>
```